Steady Harbor contracting website

I need a website for my storm restoration/roofing contracting company. Looking for design that is in current style with professional details that aren't slammed together. i need something easy to edit my self to keep it fresh and up to date on current information and product. Website needs to have visible and easy to ready contents while keeping the modern, unique, specific, and high quality looks also easy to navigate between pages. My ideal targeted customer are more on the higher end simply due to the work being detailed and most the time custom and modern.

Website needs:

1. Services tab
Inspections - Drone Inspections with AI Damage detections with VORLIX Software to inspect roofs after storms have impacted customer properties and also annual inspection roofs of every thing on the roof in minutes without having to climb roof manually leading to potential damage.

Residential - Roofing, Roof Repairs, Gutters, Siding, Paint, Decks, and Interior

Commerical - Roofing, Roof Coatings, Roof Maintenance Repair Plans, Roof Repairs, Roofing Gutters, Siding

Those are my most important services that i can think of right now, please set it how ever you think it needs to be set up for easy navigation.

2. Products
Steady Harbor doesn't look at a roof as just a roof. We look at the small details others may ignore or simply dont know anything about them. When we install a roof for clients/customer they are getting a full roofing system that includes only one manufacture per customer selection which qualities every roof installed for the highest material and labor warranty the top material manufactures offer. Steady Harbor carries the highest ranking Certifications with the leading manufacture so our customer can rest easy knowing their roofs were installed with precision.

Brands we love
Brindlecoat Summit
KRV
Le Marlo

3. Gallery/Recent Projects

Link to crew snap or create folders or whatever for photos to be added weekly or bi weekly

4 . Service Area Map

5. About Us / The Steady Harbor Team

I do not have a domain yet looking for ideas on that as well. The website domain will also be used as the business email @'s

Files attached is the logos and business cards to get idea of the company colors and styles, open to whatever though and will consider everything if it catches my eye and is appealing.

Target Market(s)

Property owners, property management companies, maintenance managers for properties, home owners, business owners, land lords

Industry/Entity Type

Roofing contractor storm restoration home remodel

Coding

Number of Pages Required

5+ page

Colors
EB3D1F
EC4F4E
F09395
F8D3D4
FCEDEE

Requirements
Must have
• Design like the KRV roofing manufacturer website or similar

```html
<!DOCTYPE html>
<html lang="en">
<head>
<meta charset="utf-8">
<title>Steady Harbor Contracting</title>
<link rel="stylesheet" href="https://fonts.googleapis.com/css2?family=Saira:wght@300;400;600;700&family=Poppins:wght@300;400;500;600&display=swap">
<style>
:root{
  --red:#d0101b;
  --red-deep:#b80d16;
  --ink:#141414;
  --text:#3a3a3a;
  --muted:#5c5c5c;
  --band:#e6e6e6;
  --white:#ffffff;
  --black:#000000;
  --line:#bdbdbd;
}
*{box-sizing:border-box;margin:0;padding:0}
html,body{width:1200px;height:4043px;overflow:hidden}
body{position:relative;background:var(--white);font-family:"Poppins",sans-serif;color:var(--text)}
.abs{position:absolute}
.heading{font-family:"Saira",sans-serif;font-weight:300;color:var(--ink);text-transform:uppercase;letter-spacing:.5px}
.heading b{font-weight:700}
.heading-bar{position:absolute;height:3px;width:52px;background:var(--red)}
.btn-outline{position:absolute;border:2px solid var(--red);border-radius:30px;color:var(--red);font-size:12px;font-weight:500;text-transform:uppercase;display:flex;align-items:center;justify-content:center;letter-spacing:.3px;background:var(--white)}
.photo{position:absolute}

/* header */
.site-header{position:absolute;left:0;top:0;width:1200px;height:78px;background:var(--white)}
.brand-plate{position:absolute;left:0;top:0;width:353px;height:78px}
.brand-name{position:absolute;left:140px;top:22px;color:var(--white);font-family:"Saira",sans-serif;font-weight:600;font-size:22px;letter-spacing:1px;text-transform:uppercase;display:flex;align-items:center;gap:8px}
.brand-dot{width:10px;height:10px;background:var(--white)}
.nav a{position:absolute;top:28px;font-size:12.5px;color:var(--ink);text-decoration:none;text-transform:uppercase;font-weight:500}
.nav .active::after{content:"";position:absolute;left:0;right:0;bottom:-12px;height:2px;background:var(--red)}
.header-phone{position:absolute;left:966px;top:26px;font-size:15px;font-weight:600;color:var(--ink);display:flex;align-items:center;gap:7px}

/* hero */
.hero{position:absolute;left:0;top:78px;width:1200px;height:554px;overflow:hidden}
.hero-title{position:absolute;left:105px;top:172px;color:var(--white);font-family:"Saira",sans-serif;font-size:31px;line-height:40px;text-transform:uppercase}
.hero-title span{display:block;font-weight:300}
.hero-title b{display:block;font-weight:700}
.hero-text{position:absolute;left:105px;top:264px;width:320px;color:var(--white);font-size:14px;line-height:22px}
.hero-btn{position:absolute;left:108px;top:335px;width:162px;height:39px;border-radius:22px;background:var(--black);color:var(--white);font-size:13px;font-weight:500;display:flex;align-items:center;justify-content:center}
.hero-dots{position:absolute;left:124px;top:407px;display:flex;gap:7px}
.hero-dots i{width:10px;height:10px;border-radius:50%;background:var(--white);border:1.5px solid var(--white)}
.hero-dots i:first-child{background:transparent}

/* services */
.service-card{position:absolute;top:786px;width:324px;height:394px;border:1px solid var(--line);background:var(--white)}
.service-card .photo{left:0;top:0;width:322px;height:215px}
.service-card h3{position:absolute;left:0;right:0;top:232px;text-align:center;font-family:"Saira",sans-serif;font-weight:600;font-size:19px;color:var(--ink);text-transform:uppercase}
.service-card p{position:absolute;left:20px;right:20px;top:268px;text-align:center;font-size:12.5px;line-height:22px;color:var(--muted)}
.service-card .btn-outline{left:85px;top:324px;width:152px;height:38px}

/* products */
.products-band{position:absolute;left:0;top:1282px;width:1200px;height:593px;background:var(--band)}
.products-copy{position:absolute;left:664px;top:1462px;width:370px}
.products-copy p{font-size:12.5px;line-height:22px;color:var(--muted);margin-top:20px}

/* about */
.about-copy p{font-size:15px;line-height:24.5px;color:var(--text);margin-bottom:24px}

/* projects */
.projects{position:absolute;left:0;top:2408px;width:1200px;height:788px;background:linear-gradient(180deg,#eef0f2,#e3e6ea)}
.project-tile{position:absolute;overflow:hidden}
.project-tile .label{position:absolute;left:30px;bottom:22px;color:var(--white);font-family:"Saira",sans-serif;font-weight:600;font-size:16px;text-transform:uppercase}
.project-tile.featured{background:var(--red)}
.project-tile.featured h4{position:absolute;left:0;right:0;top:84px;text-align:center;color:var(--white);font-family:"Saira",sans-serif;font-weight:600;font-size:16px;text-transform:uppercase}
.project-tile.featured p{position:absolute;left:50px;right:50px;top:116px;text-align:center;color:var(--white);font-size:13px;line-height:22px}

/* footer */
.site-footer{position:absolute;left:0;top:3706px;width:1200px;height:337px;background:var(--black);color:var(--white)}
.footer-col{position:absolute;top:72px}
.footer-col h5{color:var(--red);font-family:"Saira",sans-serif;font-weight:600;font-size:17px;margin-bottom:6px}
.footer-col li{list-style:none;font-size:11px;line-height:22px}
.socials{position:absolute;left:170px;top:139px;display:flex;gap:7px}
.socials i{width:22px;height:22px;border:1.5px solid var(--white);border-radius:50%}
.contact-row{display:flex;align-items:center;gap:14px;font-size:11px;line-height:14px;margin-top:8px}
</style>
</head>
<body>

<header class="site-header">
  <svg class="brand-plate" viewBox="0 0 353 78"><polygon points="0,0 353,0 314,78 0,78" fill="#000"/></svg>
  <div class="brand-name"><span class="brand-dot"></span>Steady Harbor</div>
  <nav class="nav">
    <a class="active" style="left:395px">Services</a>
    <a style="left:499px">Products</a>
    <a style="left:612px">Gallery</a>
    <a style="left:711px">Service Area</a>
    <a style="left:844px">About Us</a>
  </nav>
  <div class="header-phone">
    <svg width="16" height="16" viewBox="0 0 24 24"><path d="M6.6 10.8a15 15 0 0 0 6.6 6.6l2.2-2.2c.3-.3.7-.4 1-.2 1.1.4 2.3.6 3.6.6.6 0 1 .4 1 1V20c0 .6-.4 1-1 1A17 17 0 0 1 3 4c0-.6.4-1 1-1h3.5c.6 0 1 .4 1 1 0 1.3.2 2.5.6 3.6.1.3 0 .7-.2 1z" fill="#d0101b"/></svg>
    (555) 214 0378
  </div>
</header>

<section class="hero">
  <div class="photo" role="img" aria-label="Roofer in a hard hat fastening metal roof panels under a blue sky" style="left:0;top:0;width:1200px;height:554px;background:linear-gradient(160deg,#6f9fd0 0%,#a9c7e3 35%,#dfe4e8 60%,#b9bec4 100%)"></div>
  <svg class="abs" style="left:0;top:0" width="600" height="554" viewBox="0 0 600 554"><polygon points="0,0 588,0 405,554 0,554" fill="#d0101b" opacity=".93"/></svg>
  <h1 class="hero-title"><span>Storm Restoration</span><b>and Roofing Service</b></h1>
  <p class="hero-text">Lorem ipsum dolor sit amet, consectetur adipiscing elit, sed do eiusmod</p>
  <div class="hero-btn">LEARN MORE</div>
  <div class="hero-dots"><i></i><i></i><i></i><i></i></div>
</section>

<h2 class="heading abs" style="left:0;width:1200px;top:700px;text-align:center;font-size:33px">Services <b>Provide</b></h2>
<div class="heading-bar" style="left:574px;top:746px"></div>

<article class="service-card" style="left:96px">
  <div class="photo" role="img" aria-label="Drone inspecting a red tile roof with a tablet showing damage detection" style="background:linear-gradient(180deg,#7fb4e6 0%,#bcd8f0 40%,#c5573a 70%,#8f3b26 100%)"></div>
  <h3>Inspections</h3>
  <p>Drone Inspections with AI Damage detections with VORLIX Software</p>
  <div class="btn-outline">Learn More</div>
</article>
<article class="service-card" style="left:439px">
  <div class="photo" role="img" aria-label="Residential house with dark shingle roof" style="background:linear-gradient(180deg,#8fb2d8 0%,#c8d8e8 40%,#3c3f44 65%,#d8d8d8 100%)"></div>
  <h3>Residential</h3>
  <p>Roofing, Roof Repairs, Gutters, Siding, Paint, Decks, and Interior</p>
  <div class="btn-outline">Learn More</div>
</article>
<article class="service-card" style="left:781px">
  <div class="photo" role="img" aria-label="Commercial building with low slope metal roof" style="background:linear-gradient(180deg,#5c9ad8 0%,#a9cdef 45%,#8aa0b6 70%,#4d6a8c 100%)"></div>
  <h3>Commerical</h3>
  <p>Roofing, Roof Coatings, Roof Maintenance Repair Plans, Roof Repairs,</p>
  <div class="btn-outline">Learn More</div>
</article>

<section class="products-band"></section>
<div class="photo" role="img" aria-label="Large home with grey siding, stone facade and shingle roof" style="left:121px;top:1378px;width:576px;height:419px;background:linear-gradient(180deg,#1f7ee0 0%,#5aa6ee 35%,#4f5d70 65%,#a89a84 100%)"></div>
<svg class="abs" style="left:560px;top:1410px" width="600" height="360" viewBox="560 1410 600 360">
  <polygon points="646,1440 1133,1440 1076,1757 590,1757" fill="#d0101b"/>
  <polygon points="635,1420 1120,1420 1067,1738 576,1738" fill="#fff"/>
</svg>
<div class="products-copy">
  <h2 class="heading" style="font-size:27px">Our <b>Products</b></h2>
  <p>Steady Harbor doesn't look at a roof as just a roof. We look at the small details others may ignore or simply dont know anything about them. When we install a roof for clients/customer they are getting a full roofing system that includes only one manufacture per custom­er selection which qualities every roof installed</p>
</div>
<div class="btn-outline" style="left:664px;top:1666px;width:152px;height:37px">Learn More</div>

<div class="photo" role="img" aria-label="Roofer with safety harness laying tiles on a steep roof" style="left:538px;top:1875px;width:662px;height:533px;clip-path:polygon(0 0,100% 0,100% 100%,187px 100%);background:linear-gradient(180deg,#4f87d8 0%,#9dbfe8 40%,#5d5a57 60%,#2e2c2b 100%)"></div>
<h2 class="heading abs" style="left:133px;top:1996px;font-size:33px">About <b>Our Company</b></h2>
<div class="heading-bar" style="left:133px;top:2038px;width:48px"></div>
<div class="about-copy abs" style="left:133px;top:2064px;width:390px">
  <p>Lorem ipsum dolor sit amet, consectetur adipiscing elit, sed do eiusmod tempor incididunt ut labore et dolore magna aliqua. Ut enim ad minim veniam</p>
  <p>Lorem ipsum dolor sit amet, consectetur adipiscing elit, sed do eiusmod tempor incididunt ut labore et dolore magna aliqua. Ut enim ad minim veniam</p>
</div>
<div class="btn-outline" style="left:127px;top:2264px;width:152px;height:37px">Learn More</div>

<section class="projects">
  <h2 class="heading abs" style="left:0;width:1200px;top:68px;text-align:center;font-size:33px">Recent <b>Projects</b></h2>
  <div class="heading-bar" style="left:578px;top:114px;width:52px"></div>
  <div class="project-tile" role="img" aria-label="House with dark shingle roof gables" style="left:121px;top:156px;width:315px;height:249px;background:linear-gradient(180deg,#6aa2dc 0%,#b7d0ea 40%,#3d4048 75%,#6c6a66 100%)"><span class="label">Project Title Here</span></div>
  <div class="project-tile featured" style="left:450px;top:156px;width:316px;height:249px"><h4>Project Title Here</h4><p>Lorem ipsum dolor sit amet, con­sectetur adipiscing elit, sed do ei­usmod tempor incididunt</p></div>
  <div class="project-tile" role="img" aria-label="Drone flying above a tiled roof" style="left:778px;top:156px;width:316px;height:249px;background:linear-gradient(180deg,#5f9ee0 0%,#c6dcf0 50%,#7a4a3a 75%,#3c2a24 100%)"><span class="label">Project Title Here</span></div>
  <div class="project-tile" role="img" aria-label="Corrugated metal roof with turbine vents" style="left:121px;top:416px;width:481px;height:250px;background:linear-gradient(180deg,#9ea7b0 0%,#d5d9dd 40%,#8e959c 75%,#5d636a 100%)"><span class="label">Project Title Here</span></div>
  <div class="project-tile" role="img" aria-label="Modern house with dark metal roof and skylights" style="left:613px;top:416px;width:482px;height:250px;background:linear-gradient(180deg,#5e97d6 0%,#c2d6ea 45%,#34373c 75%,#1f2124 100%)"><span class="label">Project Title Here</span></div>
</section>

<div class="photo" role="img" aria-label="Street map of the service area with location pins" style="left:532px;top:3259px;width:551px;height:389px;background:linear-gradient(135deg,#e6e8ec 0%,#f2f3f5 50%,#dfe3e8 100%)"></div>
<svg class="abs" style="left:80px;top:3290px" width="580" height="345" viewBox="80 3290 580 345">
  <defs><filter id="panelShadow" x="-10%" y="-10%" width="120%" height="130%"><feDropShadow dx="0" dy="6" stdDeviation="10" flood-color="#000" flood-opacity=".14"/></filter></defs>
  <polygon points="151,3298 640,3298 598,3618 96,3618" fill="#fff" filter="url(#panelShadow)"/>
</svg>
<h2 class="heading abs" style="left:195px;top:3358px;font-size:28px">Service Area <b>Map</b></h2>
<p class="abs" style="left:195px;top:3418px;width:390px;font-size:13px;line-height:22px;color:var(--muted)">Lorem ipsum dolor sit amet, consectetur adipiscing elit, sed do eiusmod tempor incididunt ut labore et dolore magna aliqua. Ut enim ad minim veniam</p>
<div class="btn-outline" style="left:195px;top:3507px;width:163px;height:39px">View Locations</div>

<footer class="site-footer">
  <div class="abs" style="left:149px;top:88px;font-family:'Saira',sans-serif;font-weight:600;font-size:21px;letter-spacing:1px;text-transform:uppercase;display:flex;align-items:center;gap:8px"><span style="width:10px;height:10px;background:#fff"></span>Steady Harbor</div>
  <div class="socials"><i></i><i></i><i></i><i></i></div>
  <div class="abs" style="left:364px;top:62px;width:1px;height:108px;background:#444"></div>
  <div class="footer-col" style="left:422px"><h5>Quick Links</h5><ul><li>About Us</li><li>Services</li><li>Service Area</li></ul></div>
  <div class="footer-col" style="left:607px"><h5>Services</h5><ul><li>Inspections</li><li>Residential</li><li>Commerical</li></ul></div>
  <div class="footer-col" style="left:769px"><h5>Links</h5><ul><li>Gallery</li><li>Products</li><li>Contact</li></ul></div>
  <div class="footer-col" style="left:927px"><h5>Contact us</h5>
    <div class="contact-row"><svg width="18" height="18" viewBox="0 0 24 24"><path d="M6.6 10.8a15 15 0 0 0 6.6 6.6l2.2-2.2c.3-.3.7-.4 1-.2 1.1.4 2.3.6 3.6.6.6 0 1 .4 1 1V20c0 .6-.4 1-1 1A17 17 0 0 1 3 4c0-.6.4-1 1-1h3.5c.6 0 1 .4 1 1 0 1.3.2 2.5.6 3.6.1.3 0 .7-.2 1z" fill="#fff"/></svg><span>Phone<br>(555) 214 0379</span></div>
    <div class="contact-row" style="margin-top:18px"><svg width="18" height="14" viewBox="0 0 24 18"><path d="M0 0h24v18H0z" fill="#fff"/><path d="M0 0l12 9 12-9" fill="none" stroke="#000" stroke-width="1.6"/></svg><span>Email Us<br>hello@steadyharbor.example</span></div>
  </div>
  <div class="abs" style="left:0;top:259px;width:1200px;height:1px;background:#333"></div>
  <p class="abs" style="left:0;width:1200px;top:276px;text-align:center;font-size:11px;color:#ccc">© 2023 Company Name | All Rights Reserved</p>
</footer>

</body>
</html>
```